Gaming company needs web presence

PLEASE NOTE: We need just a simple web site. We are at least a year away from launching our first product, so the site only needs a small amount of information on it. The only people who will be visiting the web site are prospective employees, prospective investors who want a little information on the company, journalists who want a little more information, and people in the games industry who will visit to read blog posts about the development of our first game.

Brindle Hollow Studios is a new gaming company that wants to change how people think about video games. We are making games that we think can be so interesting to watch that people might want to tune into them instead of the TV.

The games we make are sophisticated, they are not for children, and we want to project an image of being serious about our craft and the brand we're trying to create. Our games are heavily focused on players interacting with each other in sophisticated ways: to negotiate, to compete, to fight, to come to each other's rescue, to cheer each other on, or to simply watch each other in awe.

We do not want a site that features lots of video game cliches like joysticks, 8 bit graphics, science fiction themes, or military themes. We are focused on craftsmanship, so we'd like to project a sense of precision, pride and deep purpose.

The purpose of this website is to create an image of our company that can help us recruit like-minded craftspeople and help find business partners. There will be no e-commerce, account creation, or forums for some time. The site should have:
-A front page that describes our business
-A section that describes our first game (we have only one for now)
-A section for employees to write blog posts. There should be something on the home page that shows links to the latest 3 blog posts.
-A section about founders that shows information about them.
-Contact information, lets people send us email

Our first game is one that looks very realistic. It takes place on a tropical island. We can't say a lot more about it in public yet, but I will say these things: it is not a game that children will play, it is not very violent, it would look more like a film than a typical video game.

And the site should be easily extendable when we have more content and more categories of content.

I've attached our official company logo with a color scheme we've been using, plus an alternate version of the logo. Please use this as a starting point for the web site's visual design. Also, I do not think it is necessary to use the dark background in the logo as the background throughout the site. I wouldn't rule it out, but I'd like to see some proposals with lighter backgrounds.

We need to be able to get code from you so that we can drop it on our server and get it running without extra effort. We need to be able to add content for Blog posts easily as well, so please indicate how that would work.
Updates

Hello everyone, Thanks for all of the great submissions so far. There are some important things I'd like to relay to everyone: We are at least a year away from launching our first game, so we only need a simple web site. Unfortunately, we can't share any screenshots or details about our first game yet. All of these submissions look great, but are far too complicated. Also, I really want to stress that we don't want to feature stock photography of people playing games, especially of children playing games. In fact, since we don't want to release any screenshots of our games and we don't have any good photography of ourselves working, it's best if there are no photographic images on the site for now.

Hello designers, Can you let me know if your designs include all the code that would let us drop the files on to our web server and easily get it up and running? Also, can you tell me how the blog posts would be created? Does your code run on a CMS? Thanks, Pellman

Hi Designers, we will be hosting this site with Wordpress, so we would prefer to have submissions ready to go on a Wordpress server. Thanks!

Target Market(s)

Investors, prospective employees, press, blog post readers.

Industry/Entity Type

Business

Font styles to use
Sans Serif

Requirements
Must have
• Simplicity first. Please use a color palette and fonts that match our logo.
Should not have
• Video game cliches. Flash animations or menus.
No children.
No photographs of people playing games.

(I realize this is very limiting, but we're keeping the sits as simple as possible for now)

```html
<!DOCTYPE html>
<html lang="en">
<head>
<meta charset="utf-8">
<title>Brindle Hollow Studios</title>
<link href="https://fonts.googleapis.com/css2?family=Oswald:wght@300;400&family=Damion&display=swap" rel="stylesheet">
<style>
:root{
  --brown-dark:#42210a;
  --brown-mid:#5a2e0e;
  --orange:#d4813f;
  --orange-text:#d07a3a;
  --script:#c9763a;
  --grey-text:#8a8a8a;
  --light-grey:#999;
  --field:#ececec;
  --white:#fff;
}
*{margin:0;padding:0;box-sizing:border-box}
html,body{width:1200px;height:1189px;overflow:hidden;background:var(--white)}
.page{position:relative;width:1280px;height:1268px;transform:scale(.9375);transform-origin:0 0;font-family:'Oswald',sans-serif;font-weight:300}
.abs{position:absolute}
/* header */
.site-header{left:0;top:0;width:1280px;height:82px;background:linear-gradient(#4a250b,#5c2f0f)}
.brand{left:100px;top:16px;color:var(--white);font-size:28px;font-weight:400;letter-spacing:1px;text-transform:uppercase;line-height:48px}
.nav{right:100px;top:0;height:82px;display:flex;align-items:center;font-size:21px;font-weight:400;color:var(--white);text-transform:uppercase}
.nav a{color:inherit;text-decoration:none;padding:0 10px;height:82px;line-height:82px}
.nav a.active{background:#3a1b06;color:var(--orange-text)}
.nav .sep{padding:0 0}
.band{left:0;top:82px;width:1280px;height:43px;background:linear-gradient(#fafafa,#eee);border-bottom:2px solid #ccc}
/* hero */
.hero{left:0;top:125px;width:1280px;height:398px;background:radial-gradient(ellipse at 62% 45%,#4a4844 0%,#2f3230 45%,#1e2120 100%)}
.hero-title{left:0;top:165px;width:1280px;text-align:center;color:var(--white);font-size:32px;font-weight:400;line-height:36px;text-transform:uppercase}
.hero-panel{left:90px;top:254px;width:350px;height:144px;background:rgba(66,33,10,.93);padding:14px 10px}
.hero-panel h2{color:var(--orange-text);font-size:29px;font-weight:400;text-transform:uppercase;line-height:34px}
.hero-panel p{color:var(--white);font-size:19px;font-weight:400;line-height:21px;margin-top:12px;letter-spacing:-.3px}
.hero-panel a{position:absolute;right:12px;bottom:6px;color:var(--white);font-size:15px;font-weight:400}
.dots{left:614px;top:347px;display:flex;gap:4px}
.dots span{width:15px;height:15px;border-radius:50%;background:var(--white)}
.dots span.on{background:var(--orange);border:2px solid var(--white)}
/* posts */
.post{top:551px;width:270px;height:312px;border:1px solid #e5e5e5;text-align:center}
.post-pic{margin:8px 8px 0;height:175px;display:flex;align-items:center;justify-content:center;color:var(--white);font-size:21px;font-weight:400;line-height:22px;text-transform:uppercase}
.pic-light{background:var(--orange)}
.pic-dark{background:var(--brown-dark)}
.post h3{color:var(--orange-text);font-size:24px;font-weight:400;margin-top:10px;line-height:30px}
.post p{color:var(--light-grey);font-size:13px;line-height:16px;margin:4px 8px 0}
.read-more{position:absolute;left:50%;transform:translateX(-50%);bottom:-7px;background:#f4f4f4;border:1px solid #ddd;color:#555;font:bold 15px Arial,sans-serif;padding:4px 7px;white-space:nowrap}
/* lower */
.script{font-family:'Damion',cursive;color:var(--script);font-size:33px;font-weight:400}
.welcome-text{left:90px;top:956px;width:458px;color:var(--grey-text);font-size:20px;line-height:23px;letter-spacing:-.2px}
.rule{height:1px;background:#aaa}
.founder{left:567px;width:320px;height:90px}
.founder-pic{position:absolute;left:0;top:0;width:80px;height:80px;background:var(--orange);border:3px solid #a34f1a;color:var(--white);font-size:17px;font-weight:400;line-height:18px;display:flex;align-items:center;justify-content:center;text-align:center}
.founder p{position:absolute;left:85px;top:3px;width:228px;font-size:9.5px;line-height:12px;color:#666;font-weight:400}
.founder a{position:absolute;left:264px;top:68px;color:var(--orange-text);font-size:11px;font-weight:400}
.divider{left:929px;top:895px;width:1px;height:312px;background:#999}
.field{left:946px;width:228px;background:var(--field);color:#aaa;font-size:12px;padding:7px 13px}
.submit{left:987px;top:1183px;width:146px;height:30px;background:var(--brown-dark);color:var(--white);font-size:18px;font-weight:400;text-align:center;line-height:30px}
/* footer */
.site-footer{left:0;top:1229px;width:1280px;height:39px;background:linear-gradient(#5a2e0e,#45230a);color:var(--white);font-weight:400}
.copy{left:109px;top:7px;font-size:17px}
.social-label{left:832px;top:4px;font-size:21px}
.social{left:1038px;top:4px;display:flex;gap:7px}
.social span{width:30px;height:30px;border-radius:50%;background:#7a7a7a}
.social span:first-child{background:#3a1b06}
</style>
</head>
<body>
<div class="page">
  <header class="site-header abs">
    <div class="brand abs">Brindle Hollow Studios</div>
    <nav class="nav abs">
      <a class="active" href="#">Home</a><span class="sep">|</span>
      <a href="#">About Us</a><span class="sep">|</span>
      <a href="#">Blog</a><span class="sep">|</span>
      <a href="#">Games</a><span class="sep">|</span>
      <a href="#">Contact Us</a>
    </nav>
  </header>
  <div class="band abs"></div>

  <section class="hero abs" role="img" aria-label="Dark cloudy backdrop with a hooded figure artwork">
    <h1 class="hero-title abs">Your header here<br>This is a sample header</h1>
    <div class="hero-panel abs">
      <h2>Lorem Ipsum</h2>
      <p>Lorem Ipsum is that it has a more-or-less normal distribution of letters, as opposed to using Content here</p>
      <a href="#">view more</a>
    </div>
    <div class="dots abs"><span></span><span></span><span class="on"></span></div>
  </section>

  <article class="post abs" style="left:90px">
    <div class="post-pic pic-light">Here is your blog<br>post pictures</div>
    <h3>POST TITILE</h3>
    <p>Lorem Ipsum is that it has a more-or-less normal distribution of letters, as opposed to using Content here,</p>
    <span class="read-more">Read More</span>
  </article>
  <article class="post abs" style="left:367px">
    <div class="post-pic pic-dark">Here is your blog<br>post pictures</div>
    <h3>POST TITILE</h3>
    <p>Lorem Ipsum is that it has a more-or-less normal distribution of letters, as opposed to using Content here,</p>
    <span class="read-more">Read More</span>
  </article>
  <article class="post abs" style="left:643px">
    <div class="post-pic pic-light">Here is your blog<br>post pictures</div>
    <h3>POST TITILE</h3>
    <p>Lorem Ipsum is that it has a more-or-less normal distribution of letters, as opposed to using Content here,</p>
    <span class="read-more">Read More</span>
  </article>
  <article class="post abs" style="left:920px">
    <div class="post-pic pic-dark">Here is your blog<br>post pictures</div>
    <h3>POST TITILE</h3>
    <p>Lorem Ipsum is that it has a more-or-less normal distribution of letters, as opposed to using Content here,</p>
    <span class="read-more">Read More</span>
  </article>

  <h2 class="script abs" style="left:92px;top:898px">Welcome to Brindle Hollow</h2>
  <p class="welcome-text abs">Lorem Ipsum is simply dummy text of the printing and type-setting industry. Lorem Ipsum has been the industry's standard dummy text ever since the 1500s, when an unknown printer took a galley of type and scrambled it to make a type specimen book. It has survived not only five centuries, but also the leap into electronic typesetting, remaining essentially unchanged. It was popularised in the 1960s with the release of Letraset sheets containing Lorem Ipsum passages, and more recently with desktop publishing software like Aldus PageMaker including versions of Lorem Ipsum</p>

  <h2 class="script abs" style="left:569px;top:898px">About Founders</h2>
  <div class="rule abs" style="left:568px;top:964px;width:341px"></div>
  <div class="founder abs" style="top:977px">
    <div class="founder-pic">founder<br>pictures<br>here</div>
    <p>Lorem Ipsum is simply dummy text of the printing and typesetting industry. Lorem Ipsum has been the industry's standard dummy text ever since the 1500s, when an unknown printer took a galley of type and scrambled it to make a type specimen book. It has survived not only five centuries,</p>
    <a href="#">read more</a>
  </div>
  <div class="rule abs" style="left:568px;top:1071px;width:341px"></div>
  <div class="founder abs" style="top:1085px">
    <div class="founder-pic">founder<br>pictures<br>here</div>
    <p>Lorem Ipsum is simply dummy text of the printing and typesetting industry. Lorem Ipsum has been the industry's standard dummy text ever since the 1500s, when an unknown printer took a galley of type and scrambled it to make a type specimen book. It has survived not only five centuries,</p>
    <a href="#">read more</a>
  </div>
  <div class="rule abs" style="left:568px;top:1179px;width:341px"></div>

  <div class="divider abs"></div>
  <h2 class="script abs" style="left:948px;top:898px">Contact Us</h2>
  <div class="field abs" style="top:956px;height:31px">name</div>
  <div class="field abs" style="top:992px;height:31px">email</div>
  <div class="field abs" style="top:1027px;height:31px">Title</div>
  <div class="field abs" style="top:1063px;height:115px">message</div>
  <div class="submit abs">Submit</div>

  <footer class="site-footer abs">
    <div class="copy abs">Brindle Hollow Studios © 2014 | Privacy Policy</div>
    <div class="social-label abs">Find Us on Social Network</div>
    <div class="social abs"><span></span><span></span><span></span><span></span></div>
  </footer>
</div>
</body>
</html>
```